Calloway needs a modernized design

We would like a modern update (that can be responsive) to our existing website. Attached are the two existing pages we would like new concepts of - our home page and a page about one of our locations.

Calloway is provides executive offices and virtual office services. Startups, law firms, and financial services are our primary clients. We would like a professional, clean design, leaning towards minimalist. We intend to greatly reduce/eliminate the long paragraphs of text.

Industry/Entity Type

Business Service

Number of Pages Required

2 page

Requirements
Must have
• A design that can be responsive
Nice to have
• Large image(s) on home page that rotate.

```html
<!DOCTYPE html>
<html lang="en">
<head>
<meta charset="utf-8">
<title>Calloway Business Centers</title>
<link href="https://fonts.googleapis.com/css2?family=Oswald:wght@400;500&family=Roboto:wght@400;500;700&display=swap" rel="stylesheet">
<style>
:root{
  --navy:#2b3a6b;
  --navy-dark:#233160;
  --ink:#1f3c6e;
  --band:#215d8a;
  --tile-navy:#1f3a7c;
  --tile-orange:#f28b20;
  --tile-red:#d5452f;
  --tile-green:#4aaa3d;
  --orange:#f28b20;
  --sky:#3aa7dc;
  --grey-bg:#f0f0f1;
  --text:#444;
  --muted:#777;
  --white:#fff;
}
*{margin:0;padding:0;box-sizing:border-box}
html,body{width:1200px;height:2594px;overflow:hidden}
body{font-family:'Roboto',Arial,sans-serif;color:var(--text);background:var(--white);position:relative}
.abs{position:absolute}

.topbar{left:0;top:0;width:1200px;height:42px;background:var(--navy);color:var(--white);font-size:13px}
.topbar .contact{left:88px;top:13px;display:flex;gap:28px;align-items:center}
.topbar .contact span{display:flex;align-items:center;gap:8px}
.topbar .social{right:88px;top:14px;display:flex;gap:6px}
.topbar .social i{display:block;width:13px;height:13px;background:var(--white);border-radius:2px}

.header{left:0;top:42px;width:1200px;height:122px;background:var(--white)}
.brand{left:86px;top:22px;display:flex;align-items:center;gap:12px}
.brand .mark{width:76px;height:76px;border-radius:50%;background:var(--ink)}
.brand .name{color:var(--ink);font-weight:500;font-size:30px;line-height:30px;letter-spacing:.5px}
.brand .name small{display:block;font-size:15px;line-height:20px;letter-spacing:1px}
.nav{right:86px;top:56px;display:flex;gap:38px;font-size:14px;color:#222;text-transform:uppercase}
.nav .active{color:var(--ink)}

.hero{left:0;top:164px;width:1200px;height:559px;background:linear-gradient(100deg,#dfe6ec 0%,#c9d2da 35%,#b58d76 60%,#6e5a52 85%,#3c3a3f 100%)}
.hero h1{left:88px;top:322px;font-family:'Oswald',Arial,sans-serif;font-weight:500;font-size:55px;line-height:64px;color:var(--ink);letter-spacing:.3px}
.hero h2{left:88px;top:390px;font-family:'Oswald',Arial,sans-serif;font-weight:400;font-size:32px;line-height:40px;color:#222}
.hero .arrows{left:88px;top:474px;display:flex;gap:8px}
.hero .arrows span{width:30px;height:30px;border-radius:50%;background:#555;display:flex;align-items:center;justify-content:center}

.welcome{left:0;top:723px;width:1200px;height:232px;background:var(--band);color:var(--white);text-align:center}
.welcome h3{position:absolute;left:0;width:1200px;top:63px;font-weight:500;font-size:26px;letter-spacing:.3px}
.welcome p{position:absolute;left:96px;width:1008px;top:108px;font-size:12.5px;line-height:21px;height:63px;overflow:hidden}

.tile{top:1003px;width:249px;height:256px;color:var(--white);text-align:center}
.tile::after{content:"";position:absolute;inset:12px;border:1px solid rgba(255,255,255,.75)}
.tile .disc{position:absolute;left:64px;top:23px;width:120px;height:120px;border-radius:50%;background:var(--white);display:flex;align-items:center;justify-content:center}
.tile .label{position:absolute;left:20px;width:209px;top:166px;font-size:17px;line-height:26px;font-weight:500;text-transform:uppercase}
.t1{left:86px;background:var(--tile-navy)}
.t2{left:344px;background:var(--tile-orange)}
.t3{left:603px;background:var(--tile-red)}
.t4{left:862px;background:var(--tile-green)}

.service{left:0;top:1335px;width:1200px;height:339px;background:var(--grey-bg)}
.service h3{left:88px;top:44px;font-size:26px;font-weight:500;color:var(--ink)}
.service p{left:88px;top:92px;width:530px;font-size:13.5px;line-height:21px;color:#333}
.service .btn{left:88px;top:255px;width:116px;height:32px;border-radius:16px;background:var(--orange);color:var(--white);font-size:11px;font-weight:500;display:flex;align-items:center;justify-content:center}
.service .photo{left:650px;top:34px;width:460px;height:270px;border:5px solid var(--white);box-shadow:0 0 3px rgba(0,0,0,.25);background:linear-gradient(90deg,#8a8275 0%,#c47a55 45%,#e8e2d8 75%,#b8b4aa 100%)}

.blog-title{left:88px;top:1746px;font-size:21px;font-weight:400;color:#222}
.blog-title b{font-weight:400;color:var(--ink)}
.blog-nav{left:690px;top:1746px}
.post{left:90px;width:626px;height:170px}
.post .thumb{position:absolute;left:0;top:0;width:216px;height:170px;border:4px solid var(--white);box-shadow:0 0 3px rgba(0,0,0,.3)}
.post .body{position:absolute;left:232px;top:10px;width:394px}
.post h4{font-size:12px;font-weight:500;color:var(--ink);text-transform:uppercase}
.post .date{font-size:11px;color:#333;margin-top:12px}
.post .text{font-size:11px;line-height:17px;color:var(--muted);margin-top:8px;height:68px;overflow:hidden}
.post .more{font-size:11px;color:var(--ink);margin-top:12px}
.p1{top:1802px}.p1 .thumb{background:linear-gradient(120deg,#e4e9ee,#8a8f99 60%,#3f4453)}
.p2{top:1999px}.p2 .thumb{background:linear-gradient(120deg,#f1ede6,#c8a98e 50%,#4c5568)}

.form{left:768px;top:1746px;width:333px;height:427px;background:var(--sky);border-radius:3px}
.form h3{position:absolute;left:0;width:333px;top:14px;text-align:center;color:var(--white);font-size:20px;font-weight:500}
.field{position:absolute;left:27px;width:279px;height:41px;background:var(--white);font-size:12px;color:#444;padding-left:13px;display:flex;align-items:center;justify-content:space-between;padding-right:14px}
.field .caret{width:0;height:0;border-left:6px solid transparent;border-right:6px solid transparent;border-top:7px solid #333}
.form .submit{position:absolute;left:27px;top:363px;width:279px;height:47px;border-radius:4px;background:linear-gradient(#555,#1e1e1e);color:var(--white);font-size:17px;display:flex;align-items:center;justify-content:center}

.rule{left:86px;top:2196px;width:1026px;height:1px;background:#e2e2e2}
.partners{left:107px;top:2250px;width:982px;display:flex;justify-content:space-between;align-items:center}
.partners i{display:block;height:38px;background:#c9c9c9;border-radius:3px}

.footer{left:0;top:2322px;width:1200px;height:211px;background:var(--navy);color:var(--white)}
.footer h5{font-size:15px;font-weight:400;text-transform:uppercase;letter-spacing:.3px}
.footer .col{top:44px}
.footer .c1{left:86px;font-size:14px;line-height:22px}
.footer .c1 .lines{margin-top:10px}
.footer .c1 .row{display:flex;align-items:center;gap:14px;margin-top:4px}
.footer .c2{left:360px}
.footer .map{margin-top:10px;width:226px;height:104px;border:3px solid #e6e6e6;background:linear-gradient(135deg,#eae6dc,#d8d4c8 50%,#efe3a8)}
.footer .c3{left:667px;width:255px}
.footer .c3 p{font-size:11.5px;line-height:20px;margin-top:12px}
.footer .sub{display:flex;margin-top:14px}
.footer .sub span{height:38px;display:flex;align-items:center;font-size:10px}
.footer .sub .in{width:171px;background:var(--white);color:#999;padding-left:14px}
.footer .sub .go{width:82px;background:var(--orange);justify-content:center;font-size:14px}
.footer .c4{left:973px}
.footer .c4 .icons{display:flex;gap:34px;margin-top:24px}
.footer .c4 .icons i{display:block;width:32px;height:32px;background:#eceef3;border-radius:3px}
.copy{left:0;top:2533px;width:1200px;height:61px;background:var(--navy-dark);color:var(--white);font-size:13px;display:flex;align-items:center;justify-content:center;border-top:1px solid rgba(255,255,255,.15)}
</style>
</head>
<body>

<div class="topbar abs">
  <div class="contact abs">
    <span><svg width="12" height="12" viewBox="0 0 12 12"><rect width="12" height="12" rx="2" fill="#fff"/><path d="M3.5 2.5l1.5 1.5-1 1c.6 1.2 1.5 2.1 2.7 2.7l1-1 1.5 1.5-1 1.3C5.5 9 3 6.5 2.4 3.6z" fill="#2b3a6b"/></svg>Dallas 214.555.0130 | Houston 713.555.0145</span>
    <span><svg width="13" height="10" viewBox="0 0 13 10"><rect width="13" height="10" rx="1" fill="#fff"/><path d="M1 1l5.5 4.5L12 1" stroke="#2b3a6b" fill="none"/></svg>info@callowaycenters.com</span>
  </div>
  <div class="social abs"><i></i><i></i><i></i><i></i><i></i></div>
</div>

<header class="header abs">
  <div class="brand abs">
    <div class="mark"></div>
    <div class="name">CALLOWAY<small>BUSINESS CENTERS</small></div>
  </div>
  <nav class="nav abs">
    <span class="active">Home</span><span>Properties</span><span>Virtual Tours &amp; Videos</span><span>Photos</span><span>Broker Referrals</span>
  </nav>
</header>

<section class="hero abs" role="img" aria-label="Team gathered at a glass board during a training session">
  <h1 class="abs">PROFESSIONAL</h1>
  <h2 class="abs">ON-DEMAND TRAINING ROOMS</h2>
  <div class="arrows abs">
    <span><svg width="10" height="12" viewBox="0 0 10 12"><path d="M7 1L2 6l5 5" stroke="#fff" stroke-width="2" fill="none"/></svg></span>
    <span><svg width="10" height="12" viewBox="0 0 10 12"><path d="M3 1l5 5-5 5" stroke="#fff" stroke-width="2" fill="none"/></svg></span>
  </div>
</section>

<section class="welcome abs">
  <h3>WELCOME TO CALLOWAY BUSINESS CENTERS</h3>
  <p>Either you need Dallas/Ft. Worth Office Space, Dallas Executive Suites, Ft. Worth Executive Suites, Houston Office Space, Houston Executive Suites, or maybe you simply need a place to stop in and use an on-demand office or meeting room from time to time or utilize our local business phone numbers, phone answering or business addresses through one of our virtual office solutions. At Calloway, you will always find affordable and beautiful, professional properties. To make decisions easy for our full service exec-</p>
</section>

<div class="tile t1 abs">
  <div class="disc"><svg width="46" height="46" viewBox="0 0 24 24"><path fill="#1f3a7c" d="M19.4 13a7.5 7.5 0 000-2l2.1-1.6-2-3.5-2.5 1a7.5 7.5 0 00-1.7-1L15 3h-4l-.4 2.7a7.5 7.5 0 00-1.7 1l-2.5-1-2 3.5L6.6 11a7.5 7.5 0 000 2l-2.1 1.6 2 3.5 2.5-1a7.5 7.5 0 001.7 1L11 21h4l.4-2.7a7.5 7.5 0 001.7-1l2.5 1 2-3.5zM13 15.5a3.5 3.5 0 110-7 3.5 3.5 0 010 7z" transform="translate(-1 0)"/></svg></div>
  <div class="label">Executive Office<br>Suites</div>
</div>
<div class="tile t2 abs">
  <div class="disc"><svg width="56" height="46" viewBox="0 0 28 22" fill="#f28b20"><circle cx="14" cy="5" r="4"/><circle cx="5" cy="8" r="3"/><circle cx="23" cy="8" r="3"/><path d="M7 21c0-5 3-8 7-8s7 3 7 8z"/><path d="M0 20c0-4 2-7 5-7 1.5 0 2.5.6 3 1.2C7 16 6.5 18 6.5 20z"/><path d="M28 20c0-4-2-7-5-7-1.5 0-2.5.6-3 1.2 1 1.8 1.5 3.8 1.5 5.8z"/></svg></div>
  <div class="label">On-Demand Meeting<br>Rooms</div>
</div>
<div class="tile t3 abs">
  <div class="disc"><svg width="54" height="46" viewBox="0 0 27 23" fill="#d5452f"><path d="M13.5 0l6 3v6l-6 3-6-3V3z"/><path d="M7 11l6 3v6l-6 3-6-3v-6z"/><path d="M20 11l6 3v6l-6 3-6-3v-6z"/></svg></div>
  <div class="label">On-Demand Training<br>Rooms</div>
</div>
<div class="tile t4 abs">
  <div class="disc"><svg width="40" height="46" viewBox="0 0 20 23" fill="#4aaa3d"><circle cx="10" cy="6" r="5.5"/><path d="M0 23c0-7 4-10 10-10s10 3 10 10z"/></svg></div>
  <div class="label">Virtual Offices<br><span style="text-transform:none">Solution</span></div>
</div>

<section class="service abs">
  <h3 class="abs">OUR SERVICE</h3>
  <p class="abs">Calloway Business Centers positions its management team in every one of its business centers - we operate with an open-door policy as a medium-sized company without all of the corporate bureaucracy and red tape.<br>The service we provide in terms of technology is unparalleled in our industry. We outfit each of our locations with 100Mbps of bandwidth! We have the latest systems in place, with all locations offering IP PBX telephone systems, Corvane IP telephones and ReachLine Technology including Voicemail to Email and ClearFax, with local technical support..</p>
  <div class="btn abs">READ MORE</div>
  <div class="photo abs" role="img" aria-label="Professional working at a laptop in a bright office"></div>
</section>

<h3 class="blog-title abs">LATEST <b>BLOG</b></h3>
<svg class="blog-nav abs" width="26" height="18" viewBox="0 0 26 18"><path d="M9 3L3 9l6 6M17 3l6 6-6 6" stroke="#222" stroke-width="2" fill="none"/></svg>

<article class="post p1 abs">
  <div class="thumb" role="img" aria-label="Colleagues reviewing a document at a desk"></div>
  <div class="body">
    <h4>Simply Dummy Text</h4>
    <div class="date">20/08/2016</div>
    <div class="text">Lorem Ipsum has been the industry's standard dummy text ever since the 1500s, when an unknown printer took a galley of type and scrambled it to make a type specimen book. It has survived not only five centuries, but also the leap into electronic typesetting, remaining essentially unchanged. It was popularised in the 1960s with</div>
    <div class="more">Read More &gt;&gt;</div>
  </div>
</article>
<article class="post p2 abs">
  <div class="thumb" role="img" aria-label="Two business people meeting at a laptop"></div>
  <div class="body">
    <h4>Simply Dummy Text</h4>
    <div class="date">20/08/2016</div>
    <div class="text">Lorem Ipsum has been the industry's standard dummy text ever since the 1500s, when an unknown printer took a galley of type and scrambled it to make a type specimen book. It has survived not only five centuries, but also the leap into electronic typesetting, remaining essentially unchanged. It was popularised in the 1960s with</div>
    <div class="more">Read More &gt;&gt;</div>
  </div>
</article>

<form class="form abs">
  <h3>REQUEST INFORMATION</h3>
  <div class="field" style="top:56px">Name</div>
  <div class="field" style="top:106px">Company Name</div>
  <div class="field" style="top:158px">Phone</div>
  <div class="field" style="top:210px">Email</div>
  <div class="field" style="top:260px">Property Interested In<span class="caret"></span></div>
  <div class="field" style="top:312px">Product Interested In<span class="caret"></span></div>
  <div class="submit">SIGNUP</div>
</form>

<div class="rule abs"></div>
<div class="partners abs">
  <i style="width:66px"></i><i style="width:120px"></i><i style="width:99px"></i><i style="width:114px"></i><i style="width:88px"></i><i style="width:123px"></i>
</div>

<footer class="footer abs">
  <div class="col c1 abs">
    <h5>Contact Us</h5>
    <div class="lines">PO BOX 4180<br>Ridgefield, Texas</div>
    <div class="row"><svg width="16" height="16" viewBox="0 0 16 16"><path d="M3 1.5l3 3-1.8 1.8c1 2 2.5 3.5 4.5 4.5L10.5 9l3 3-2 2.5C6.5 14 2 9.5 1.5 4.5z" stroke="#fff" fill="none" stroke-width="1.3"/></svg>+1 956-555-0187</div>
    <div class="row" style="font-size:13px"><svg width="16" height="12" viewBox="0 0 16 12"><rect x=".7" y=".7" width="14.6" height="10.6" stroke="#fff" fill="none" stroke-width="1.3"/><path d="M1 1l7 6 7-6" stroke="#fff" fill="none" stroke-width="1.3"/></svg>info@callowaycenters.com</div>
  </div>
  <div class="col c2 abs">
    <h5>Location</h5>
    <div class="map" role="img" aria-label="Street map showing the office location"></div>
  </div>
  <div class="col c3 abs">
    <h5>Newsletter</h5>
    <p>Excepteur sint occaecat cupidatat non proident, sunt in culpa qui officia deserunt mollit anim</p>
    <div class="sub"><span class="in">Enter your email address</span><span class="go">Sign Up</span></div>
  </div>
  <div class="col c4 abs">
    <h5>Social Media</h5>
    <div class="icons"><i></i><i></i><i></i></div>
  </div>
</footer>
<div class="copy abs">2016&nbsp; All Rights Reserved.</div>

</body>
</html>
```